Stationary Design - KM Facial Plastics

We are looking for a stylish and professional stationary design for a facial plastic surgeon. The stationary design will be for letterhead, business card, appointment cards and envelopes.
The design must be slick and aesthetically pleasing whilst incorporating the style of our logo as attached below.

Target Market(s)

Adults of all ages

Font styles to use
Serif
Script

Requirements
Must have
• Must be an aesthetically pleasing, stylish and professional design that includes the required information in a captivating layout.
• Must also be welcoming with a balanced design and a clean crisp finish.
• Details should include:
• Mr Dorian Halvet - Consultant Otolaryngologist & Facial Plastic Surgeon
• Phone: 03 5917 2846
• Fax: 03 5918 4072
• Email: info@kmfacialplastics.example.au
• Consulting from: Ashgrove, Kelton, Marlow Vale, Fenwick & Harbour City
• Appointment Card should include:
• Date, time, fee and location as per the attached example.
• location addresses are:
• 41 Marlow Street Kelton Vic 3564
• 318 Bramble Street Ashgrove Vic 3550
• Level 3, 612 Hadley Street, Marlow Vale Vic 3076
• Level 6, 480 Tennant Street Melbourne Vic 3000
Should not have
• Clutter

```html
<!DOCTYPE html>
<html lang="en">
<head>
<meta charset="utf-8">
<title>KM Facial Plastics – Stationery</title>
<link href="https://fonts.googleapis.com/css2?family=Cinzel:wght@400&family=Roboto:wght@400;500&family=Work+Sans:wght@300;400&display=swap" rel="stylesheet">
<style>
  :root{
    --backdrop:#cfcfcf;
    --paper:#ffffff;
    --ink:#2e2e2e;
    --ink-soft:#555555;
    --flap:#414141;
    --on-flap:#e9e9e9;
    --shadow:rgba(0,0,0,.35);
  }
  *{margin:0;padding:0;box-sizing:border-box}
  html,body{width:1200px;height:751px;overflow:hidden;background:var(--backdrop)}
  body{position:relative;font-family:"Work Sans",sans-serif;color:var(--ink)}
  .sheet{position:absolute;background:var(--paper);box-shadow:2px 2px 3px var(--shadow)}

  .brand{position:absolute;display:flex;align-items:center;gap:6px;font-family:"Cinzel",serif;color:var(--ink);white-space:nowrap;letter-spacing:.04em}
  .brand-dot{border:1px solid currentColor;border-radius:50%;flex:none}

  /* letterhead */
  .letterhead{left:71px;top:27px;width:493px;height:697px}
  .letterhead .brand{left:31px;top:62px;font-size:13px}
  .letterhead .brand-dot{width:16px;height:16px}
  .contact-list{position:absolute;right:34px;top:47px;list-style:none;text-align:right;font-size:8.6px;line-height:11.7px;color:var(--ink)}
  .contact-list li{display:flex;justify-content:flex-end;align-items:center;gap:6px}
  .contact-list svg{width:7px;height:7px;flex:none}
  .salutation{position:absolute;left:33px;top:189px;font-size:11.5px}
  .letter-body{position:absolute;left:33px;top:227px;width:440px;font-size:9.2px;line-height:13px;font-weight:300;color:var(--ink-soft);white-space:nowrap}
  .letter-body p{margin-bottom:16px}
  .letter-body p.tight{margin-bottom:13px}
  .sign-off{position:absolute;left:33px;top:516px;font-size:11.5px}
  .signatory{position:absolute;left:33px;top:537px;font-size:11px}
  .signatory small{display:block;font-size:8.4px;margin-top:1px}

  /* business card */
  .business-card{left:631px;top:26px;width:236px;height:134px}
  .business-card .brand{left:10px;top:62px;font-size:5.6px;gap:3px;letter-spacing:.02em}
  .business-card .brand-dot{width:8px;height:8px}
  .card-divider{position:absolute;left:99px;top:35px;width:1px;height:63px;background:var(--ink)}
  .card-name{position:absolute;left:109px;top:34px;font-family:"Roboto",sans-serif;font-weight:500;font-size:11.5px}
  .card-role{position:absolute;left:109px;top:48px;font-family:"Roboto",sans-serif;font-size:5.4px;line-height:7.8px}
  .card-contacts{position:absolute;left:109px;top:69px;list-style:none;font-family:"Roboto",sans-serif;font-size:5.4px;line-height:7.8px}
  .card-contacts li{display:flex;align-items:center;gap:3px}
  .card-contacts svg{width:4.5px;height:4.5px}

  /* appointment card */
  .appointment-card{left:906px;top:26px;width:235px;height:134px;font-family:"Cinzel",serif;font-size:7.6px}
  .day-row{position:absolute;left:13px;right:13px;top:42px;display:flex;justify-content:space-between}
  .day-row span{display:flex;align-items:center;gap:3px}
  .day-row span::before{content:"";width:5px;height:5px;border:.8px solid var(--ink)}
  .date-time{position:absolute;left:13px;top:71px;font-size:8.4px;display:flex;align-items:baseline}
  .blank{display:inline-block;border-bottom:.8px solid var(--ink);margin:0 1px}
  .meridiem{position:absolute;right:14px;top:68px;text-align:right;font-size:8.4px;line-height:12px}
  .consulting{position:absolute;left:0;right:0;top:106px;text-align:center;font-size:6.4px;line-height:10px}

  /* envelopes */
  .envelope-back{left:631px;top:189px;width:510px;height:255px}
  .flap{position:absolute;left:0;top:0;width:510px;height:65px}
  .envelope-back .brand{left:50%;top:27px;transform:translateX(-50%);font-size:7.5px;color:var(--on-flap);gap:4px}
  .envelope-back .brand-dot{width:9px;height:9px}
  .envelope-front{left:631px;top:470px;width:510px;height:254px}
  .envelope-front .brand{left:20px;top:55px;font-size:13px}
  .envelope-front .brand-dot{width:16px;height:16px}
  .envelope-consulting{position:absolute;left:20px;top:212px;font-family:"Cinzel",serif;font-size:9.4px;line-height:15px;letter-spacing:.02em}
</style>
</head>
<body>

<section class="sheet letterhead">
  <div class="brand"><span class="brand-dot"></span>KM Facial Plastics</div>
  <ul class="contact-list">
    <li>03 5917 2846 <svg viewBox="0 0 10 10"><path d="M2 1l2 2-1 1.5q1 2 2.5 2.5L7 6l2 2-1.5 1.5Q3 8 .5 2.5z" fill="none" stroke="#2e2e2e"/></svg></li>
    <li>03 5918 4072 <svg viewBox="0 0 10 10"><rect x="2.5" y=".5" width="5" height="9" rx="1" fill="none" stroke="#2e2e2e"/></svg></li>
    <li>admin@harbourentclinic.example.au <svg viewBox="0 0 10 10"><rect x=".5" y="2" width="9" height="6" fill="none" stroke="#2e2e2e"/><path d="M.5 2l4.5 3.5L9.5 2" fill="none" stroke="#2e2e2e"/></svg></li>
    <li>318 Bramble Street Ashgrove <svg viewBox="0 0 10 10"><path d="M5 9.5Q1.5 5.5 1.5 3.5a3.5 3.5 0 0 1 7 0Q8.5 5.5 5 9.5z" fill="#2e2e2e"/><circle cx="5" cy="3.5" r="1.2" fill="#fff"/></svg></li>
  </ul>
  <p class="salutation">Dear sir/Madam,</p>
  <div class="letter-body">
    <p>Lorem ipsum dolor sit amet, an vel recteque dissentiet, detracto albucius platonem ex vel,<br>eros repudiandae cu. Atqui aliquando nec an, unum graece adolescens vel ad. Id odio scae<br>has, iudico euismod atomorum ius ea, cum ea honestatis quaerendum theophrastus. Mea<br>honestatis quaerendum theophrastus. Mea</p>
    <p>Lorem ipsum dolor sit amet, an vel recteque dissentiet, detracto albucius platonem ex vel,<br>eros repudiandae cu. Atqui aliquando nec an, unum graece adolescens vel ad. Id odio scae<br>has, iudico euismod atomorum ius ea, cum ea honestatis quaerendum theophrastus. Mea<br>doming repudiandae ex, cu cum civibus assentior posidonium. Quo etiam pertinax ex, te<br>eros repudiandae cu. Atqui aliquando nec an, unum graece adolescens vel ad. Id odio scae<br>honestatis quaerendum theophrastus. Mea</p>
    <p class="tight">Lorem ipsum dolor sit amet, an vel recteque dissentiet, detracto albucius platonem ex vel,<br>eros repudiandae cu. Atqui aliquando nec an, unum graece adolescens vel ad. Id odio scae<br>has, iudico euismod atomorum ius ea, cum ea honestatis quaerendum theophrastus. Mea<br>honestatis quaerendum theophrastus. Mea</p>
    <p>eros repudiandae cu. Atqui aliquando nec an, unum graece adolescens vel ad. Id odio scae<br>honestatis quaerendum theophrastus. Mea posidonium. Quo etiam pertinax ex, te<br>etiam pertinax ex, te</p>
  </div>
  <p class="sign-off">Kind Regards</p>
  <p class="signatory">Lionel P. Marsh<small>CEO / Founder</small></p>
</section>

<section class="sheet business-card">
  <div class="brand"><span class="brand-dot"></span>KM Facial Plastics</div>
  <div class="card-divider"></div>
  <p class="card-name">Mr Dorian Halvet</p>
  <p class="card-role">Consultant Otolaryngologist<br>&amp; Facial Plastic Surgeon</p>
  <ul class="card-contacts">
    <li><svg viewBox="0 0 10 10"><path d="M2 1l2 2-1 1.5q1 2 2.5 2.5L7 6l2 2-1.5 1.5Q3 8 .5 2.5z" fill="#2e2e2e"/></svg>03 5917 2846</li>
    <li><svg viewBox="0 0 10 10"><rect x="2.5" y=".5" width="5" height="9" rx="1" fill="none" stroke="#2e2e2e" stroke-width="1.5"/></svg>03 5918 4072</li>
    <li><svg viewBox="0 0 10 10"><rect x=".5" y="2" width="9" height="6" fill="none" stroke="#2e2e2e" stroke-width="1.5"/></svg>admin@harbourentclinic.example.au</li>
    <li><svg viewBox="0 0 10 10"><path d="M5 9.5Q1.5 5.5 1.5 3.5a3.5 3.5 0 0 1 7 0Q8.5 5.5 5 9.5z" fill="#2e2e2e"/></svg>318 Bramble Street Ashgrove</li>
  </ul>
</section>

<section class="sheet appointment-card">
  <div class="day-row"><span>Mon</span><span>Tues</span><span>Wed</span><span>Thurs</span><span>Fri</span><span>Sat</span></div>
  <div class="date-time">Date&nbsp;<span class="blank" style="width:86px"></span>Time<span class="blank" style="width:54px"></span></div>
  <div class="meridiem">A.M.<br>P.M.</div>
  <p class="consulting">Consulting from:<br>Ashgrove, Kelton, Marlow Vale, Fenwick &amp; Harbour City</p>
</section>

<section class="sheet envelope-back">
  <svg class="flap" viewBox="0 0 510 65" aria-hidden="true"><path d="M0 0H510V18Q500 35 490 50Q478 64 462 64H48Q32 64 20 50Q10 35 0 18Z" fill="var(--flap)"/></svg>
  <div class="brand"><span class="brand-dot"></span>KM Facial Plastics</div>
</section>

<section class="sheet envelope-front">
  <div class="brand"><span class="brand-dot"></span>KM Facial Plastics</div>
  <p class="envelope-consulting">Consulting from:<br>Ashgrove, Kelton, Marlow Vale, Fenwick &amp; Harbour City</p>
</section>

</body>
</html>
```